Brisbane IT support business needs our first website

Hi All,

We are after a new website design for our IT solutions and support business.The business name is Harlow Digital Systems Group, or HDSG for short. We provide a range of solutions and services within the IT space.

I would like to utilize the two colours in our business logo I have uploaded.

I understand this is initially for the design only aspect of the site, but I would like to engage the winner to finish coding the website and finalize after also.

Target Market(s)

Other businesses owners and home users.

Industry/Entity Type

Business

Requirements
Must have
• Nice clean and functional design utilizing our business colours from the logo.

```html
<!DOCTYPE html>
<html lang="en">
<head>
<meta charset="utf-8">
<title>Harlow Digital Systems Group</title>
<link href="https://fonts.googleapis.com/css2?family=Open+Sans:wght@300;400;600;700&display=swap" rel="stylesheet">
<style>
:root{
  --orange:#f07b1e;
  --navy:#0f4a66;
  --text:#6f6f6f;
  --dark:#333;
  --line:#c9ced3;
  --panel:#f2f2f2;
  --footer:#2b2b2b;
  --footer-text:#c9c9c9;
  --partner:#9a9a9a;
}
*{margin:0;padding:0;box-sizing:border-box}
html,body{width:789px;height:1200px;overflow:hidden;background:#fff}
body{position:relative;font-family:"Open Sans",Arial,sans-serif;color:var(--text)}
.abs{position:absolute}

.hero{left:0;top:0;width:789px;height:423px;background:linear-gradient(180deg,#dfe7ef 0%,#c4d1de 45%,#9fb0c2 70%,#b7a898 100%)}
.hero-person{left:370px;top:95px;width:330px;height:328px;border-radius:40% 40% 10% 10%;background:linear-gradient(180deg,#e9ecef 0%,#cfd4d9 60%,#2a2a2a 100%);opacity:.55}
.hero-title{left:87px;top:183px;font-size:21.5px;font-weight:300;line-height:25px;color:#1e1e1e}
.hero-arrow{top:200px}

.header{left:66px;top:0;width:657px;height:80px;background:#fff}
.header-rule{left:66px;top:79px;width:657px;height:3px;background:var(--orange)}
.brand{left:73px;top:17px;display:flex;align-items:center;gap:8px}
.brand-mark{width:54px;height:54px;border-radius:50%;background:var(--navy)}
.brand-name{font-size:26px;font-weight:700;color:var(--orange);letter-spacing:.5px}
.nav{top:50px;display:flex;font-size:9.5px;text-transform:uppercase;color:#777}
.nav a{position:absolute;white-space:nowrap;text-decoration:none;color:inherit}
.nav a.active{color:var(--navy)}
.nav-marker{left:298px;top:77px;width:35px;height:5px;background:var(--navy)}

.welcome-title{left:0;top:453px;width:789px;text-align:center;font-size:20.5px;font-weight:700;color:var(--orange)}
.welcome-text{left:96px;top:484px;width:597px;text-align:center;font-size:8.6px;line-height:15.2px}
.btn{display:flex;align-items:center;justify-content:center;border-radius:4px;font-size:8.6px;text-transform:uppercase;background:#fff}
.btn-more{left:359px;top:561px;width:71px;height:27px;border:1.5px solid var(--orange);color:var(--orange)}

.services-title{left:0;top:625px;width:789px;text-align:center;font-size:20px;font-weight:700;color:var(--navy)}
.services-rule{top:638px;height:1px;background:var(--line)}
.service{top:662px;width:151px;text-align:center}
.service-photo{width:151px;height:138px}
.service-name{margin-top:9px;font-size:12.3px;font-weight:700;color:var(--navy);text-transform:uppercase}
.service-desc{margin-top:1px;font-size:8.3px;line-height:12.5px}

.divider{left:66px;top:869px;width:657px;height:1px;background:#bdbdbd}
.help{left:66px;top:874px;width:657px;height:157px;background:var(--panel)}
.help-icon{left:385px;top:887px}
.help-title{left:0;top:912px;width:789px;text-align:center;font-size:17px;font-weight:600;color:var(--dark)}
.help-text{left:0;top:942px;width:789px;text-align:center;font-size:10.4px;line-height:14px;color:#7a7a7a}
.btn-contact{left:359px;top:986px;width:71px;height:27px;border:1.5px solid var(--navy);color:var(--navy)}

.partners{left:66px;top:1064px;width:657px;display:flex;justify-content:space-between;align-items:center;font-size:14px;font-weight:600;color:var(--partner)}

.footer{left:0;top:1117px;width:789px;height:83px;background:var(--footer)}
.footer-links{left:66px;top:1139px;font-size:9px;color:var(--footer-text);word-spacing:1px}
.footer-links span{margin:0 6px;color:#8b8b8b}
.copyright{left:66px;top:1161px;font-size:9px;color:var(--footer-text)}
.social{left:638px;top:1149px;display:flex;gap:4px}
.social i{display:block;width:18px;height:18px;border-radius:2px;background:#e6e6e6}
</style>
</head>
<body>

<div class="abs hero" role="img" aria-label="Photo of a cheering businessman sitting cross-legged with a laptop on a rock in front of misty mountains"></div>
<div class="abs hero-person" role="img" aria-label="Businessman with raised arms and laptop"></div>
<h1 class="abs hero-title">We are IT solutions and<br>support company.</h1>
<svg class="abs hero-arrow" style="left:13px" width="14" height="22" viewBox="0 0 14 22"><path d="M11 2 3 11l8 9" fill="none" stroke="#eef2f6" stroke-width="2"/></svg>
<svg class="abs hero-arrow" style="left:762px" width="14" height="22" viewBox="0 0 14 22"><path d="M3 2l8 9-8 9" fill="none" stroke="#eef2f6" stroke-width="2"/></svg>

<header>
  <div class="abs header"></div>
  <div class="abs header-rule"></div>
  <div class="abs brand"><span class="brand-mark"></span><span class="brand-name">HDSG</span></div>
  <nav class="abs nav">
    <a class="active" style="left:301px">Home</a>
    <a style="left:359px">About us</a>
    <a style="left:436px">Services</a>
    <a style="left:507px">Solutions</a>
    <a style="left:590px">Clients</a>
    <a style="left:657px">Contact us</a>
  </nav>
  <div class="abs nav-marker"></div>
</header>

<h2 class="abs welcome-title">WELCOME TO HDSG</h2>
<p class="abs welcome-text">Aenean porta metus lorem, in gravida orci finibus in. Fusce sodales consectetur metus et ultricies. Nulla sit amet augue in arcu ultrices placerat. Nam nec convallis nisi, porta facilisis ante. Praesent pretium, sem vehicula aliquam rhoncus, ipsum turpis pharetra odio, in commodo nisi urna laoreet felis. Pellentesque et lacus laoreet, blandit erat non, feugiat tortor. Aliquam sed dignissim velit, vitae tincidunt lectus. Integer laoreet sollicitudin porttitor dolor sit amet.</p>
<a class="abs btn btn-more">Read more</a>

<div class="abs services-rule" style="left:66px;width:269px"></div>
<h2 class="abs services-title">SERVICES</h2>
<div class="abs services-rule" style="left:453px;width:270px"></div>

<section>
  <div class="abs service" style="left:66px">
    <div class="service-photo" role="img" aria-label="Businessman holding red puzzle pieces over a desk" style="background:linear-gradient(180deg,#1c1f2b 0%,#3a2a26 60%,#b07a4a 100%)"></div>
    <h3 class="service-name">Aenean porta</h3>
    <p class="service-desc">Fusce sodales consectetur<br>metus et ultricies</p>
  </div>
  <div class="abs service" style="left:235px">
    <div class="service-photo" role="img" aria-label="Woman on the phone holding a red folder in an office" style="background:linear-gradient(180deg,#eef0f2 0%,#c9c2b8 55%,#2a2a2e 100%)"></div>
    <h3 class="service-name">Fusce sodales</h3>
    <p class="service-desc">Fusce sodales consectetur<br>metus et ultricies</p>
  </div>
  <div class="abs service" style="left:403px">
    <div class="service-photo" role="img" aria-label="Smiling man working with a calculator and files at a desk" style="background:linear-gradient(180deg,#f1f1f1 0%,#b8b3ad 50%,#2e3440 80%,#d9d6d0 100%)"></div>
    <h3 class="service-name">Suspendisse vel</h3>
    <p class="service-desc">Fusce sodales consectetur<br>metus et ultricies</p>
  </div>
  <div class="abs service" style="left:572px">
    <div class="service-photo" role="img" aria-label="Man drawing a checklist on a glass board" style="background:linear-gradient(90deg,#f4f4f4 0%,#e4e4e4 55%,#c7b3a4 85%,#d8dde2 100%)"></div>
    <h3 class="service-name">Quisque ultricies</h3>
    <p class="service-desc">Fusce sodales consectetur<br>metus et ultricies</p>
  </div>
</section>

<div class="abs divider"></div>
<section>
  <div class="abs help"></div>
  <svg class="abs help-icon" width="20" height="20" viewBox="0 0 20 20" aria-hidden="true">
    <circle cx="10" cy="10" r="8.5" fill="none" stroke="#3a3a3a" stroke-width="3"/>
    <circle cx="10" cy="10" r="3.2" fill="#fff" stroke="#3a3a3a" stroke-width="1.5"/>
    <path d="M4 4l3 3M16 4l-3 3M4 16l3-3M16 16l-3-3" stroke="#fff" stroke-width="2"/>
  </svg>
  <h2 class="abs help-title">NEED HELP?</h2>
  <p class="abs help-text">Proin imperdiet ante id velit auctor, vitae ullamcorper purus finibus.<br>Quisque ut purus enim. Proin nec turpis orci. Donec venenatis libero tortor, sed volutpat lacus porttitor</p>
  <a class="abs btn btn-contact">Contact us</a>
</section>

<div class="abs partners">
  <span>Marlowe</span><span>Quintara</span><span>Netlyne</span><span>Orvo</span><span>Kestrix</span><span>Telmora</span><span>Vantrix</span><span>Pellum</span><span>Corvex</span>
</div>

<footer>
  <div class="abs footer"></div>
  <p class="abs footer-links">Home<span>|</span>About us<span>|</span>Services<span>|</span>Solutions<span>|</span>Clients<span>|</span>Contact us</p>
  <p class="abs copyright">Copyright &copy; 2014 &nbsp;Harlow Digital Systems Group. &nbsp;All rights reserved.</p>
  <div class="abs social">
    <i></i><i></i><i></i>
    <svg width="18" height="18" viewBox="0 0 18 18" aria-label="Email"><rect width="18" height="18" rx="2" fill="#e6e6e6"/><rect x="4" y="5.5" width="10" height="7" fill="#555"/><path d="M4 5.5l5 4 5-4" fill="none" stroke="#e6e6e6" stroke-width="1"/></svg>
  </div>
</footer>

</body>
</html>
```